Flyer design for the Harvest Lantern Summit 2019 (HALSUM)

Design a flyer for our annual conference with basic information about the conference: conference logo and year, Conference name: Harvest Lantern Summit Location: Talbot Community Center (Downtown Portland)482 Wexley Street, Portland, ME 04109, Date: August 8th, 9th, 10th and 11th, 2019Start time 7:00PMI would like the following three words added to the flyer. These words describe the vision of the conference: Prophetic, Fire, Overflow,

Contact info:
Website: www.vostel.org
Phone: 207 555 3184
Email: contact@meadowcrest.org

Target Market(s)

Young adults living in the United States

Industry/Entity Type

Religious

Font styles to use
Sans Serif

Colors

Designer to choose colors to be used in the design.

Requirements
Must have
• HALSUM must logo standout, the reader should be able to take a quick look and find key info,
Should not have
• Cross image, church image

```html
<!DOCTYPE html>
<html lang="en">
<head>
<meta charset="utf-8">
<title>Harvest Lantern Summit 2019 – Flyer</title>
<link href="https://fonts.googleapis.com/css2?family=Montserrat:wght@600&family=Oswald:wght@600&family=Arimo:wght@400;700&display=swap" rel="stylesheet">
<style>
  :root{
    --page-bg:#9a9a9a;
    --paper:#ffffff;
    --brand-blue:#1273bb;
    --brand-orange:#f7941d;
    --ink:#1d1d1d;
    --photo-dark:#2c2218;
    --photo-mid:#6b3a14;
    --photo-warm:#c25a12;
  }
  *{margin:0;padding:0;box-sizing:border-box}
  html,body{width:1200px;height:1200px;overflow:hidden;background:var(--page-bg)}
  .flyer{
    position:absolute;left:190px;top:25px;
    width:963px;height:1350px;
    transform:scale(.8515);transform-origin:0 0;
    background:var(--paper);overflow:hidden;
    font-family:"Arimo",Arial,sans-serif;color:var(--ink);
  }
  .flyer-shapes{position:absolute;inset:0}
  .logo{
    position:absolute;left:0;width:942px;top:352px;text-align:center;
    font-family:"Montserrat",sans-serif;font-weight:600;color:#fff;
  }
  .logo-name{font-size:98px;letter-spacing:2px;line-height:1}
  .logo-year{
    display:flex;align-items:center;justify-content:center;gap:14px;
    margin-top:10px;font-size:44px;letter-spacing:26px;
  }
  .logo-year::before,.logo-year::after{content:"";width:118px;height:3px;background:#fff}
  .logo-year span{margin-right:-26px}
  .event-title{
    position:absolute;left:0;width:976px;top:806px;text-align:center;
    font-family:"Oswald",sans-serif;font-weight:600;font-size:126px;line-height:1;
    color:var(--brand-blue);letter-spacing:1px;
  }
  .event-subtitle{
    position:absolute;left:0;width:976px;top:926px;text-align:center;
    font-family:"Arimo",sans-serif;font-weight:700;font-size:38px;
    color:var(--brand-orange);letter-spacing:.5px;
  }
  .venue{position:absolute;left:0;width:968px;top:1008px;text-align:center}
  .venue svg{display:block;margin:0 auto 12px}
  .venue-address{font-size:24px;line-height:30px}
  .schedule{
    position:absolute;left:111px;width:698px;top:1163px;height:59px;
    border-top:2px solid var(--brand-blue);border-bottom:2px solid var(--brand-blue);
    display:flex;align-items:center;font-size:24px;
  }
  .schedule-item{display:flex;align-items:center;gap:9px;position:absolute}
  .schedule-date{left:46px}
  .schedule-time{left:524px}
  .contact-bar{position:absolute;left:0;top:1276px;width:963px;height:74px;color:#fff}
  .contact-item{position:absolute;display:flex;align-items:center;gap:10px;top:0;height:74px}
  .contact-phone{left:52px;font-family:"Oswald",sans-serif;font-size:28px;letter-spacing:.5px}
  .contact-email{left:303px;font-size:18px;top:-6px}
  .contact-web{left:680px;font-size:18px;top:-6px}
</style>
</head>
<body>
<main class="flyer">
  <svg class="flyer-shapes" width="963" height="1350" viewBox="0 0 963 1350">
    <defs>
      <linearGradient id="photoTone" x1="0" y1="0" x2="1" y2="0.3">
        <stop offset="0" stop-color="var(--photo-dark)"/>
        <stop offset="0.55" stop-color="var(--photo-mid)"/>
        <stop offset="1" stop-color="var(--photo-warm)"/>
      </linearGradient>
    </defs>
    <path class="orange-sweep" fill="var(--brand-orange)"
      d="M70 985 C20 850 30 680 130 540 L300 640 C180 740 100 850 70 985 Z"/>
    <circle class="hero-photo" role="img" aria-label="Photo: silhouette of a person with raised arms against a warm sunset sky"
      cx="476" cy="184" r="536" fill="url(#photoTone)"/>
    <path class="pin-accent" d="M0 0 H963 V0 Z" fill="none"/>
    <rect class="footer-band" x="0" y="1280" width="963" height="70" fill="var(--brand-blue)"/>
    <path class="footer-gap" fill="#fff" d="M240 1280 H930 C905 1300 900 1340 850 1342 H290 C265 1342 262 1300 240 1280 Z"/>
    <path class="footer-orange" fill="var(--brand-orange)" d="M256 1287 H916 C895 1305 890 1333 850 1333 H292 C272 1333 270 1305 256 1287 Z"/>
  </svg>

  <div class="logo">
    <div class="logo-name">HALSUM</div>
    <div class="logo-year"><span>2019</span></div>
  </div>

  <h1 class="event-title">HARVEST 2019</h1>
  <p class="event-subtitle">HARVEST LANTERN SUMMIT</p>

  <section class="venue">
    <svg width="26" height="34" viewBox="0 0 26 34" aria-hidden="true">
      <path d="M13 2a9 9 0 0 0-9 9c0 7 9 16 9 16s9-9 9-16a9 9 0 0 0-9-9z" fill="none" stroke="var(--brand-orange)" stroke-width="2.5"/>
      <circle cx="13" cy="11" r="3.5" fill="var(--brand-orange)"/>
      <ellipse cx="13" cy="30" rx="10" ry="2.5" fill="none" stroke="var(--brand-orange)" stroke-width="1.5"/>
    </svg>
    <p class="venue-address">Talbot Community Center (Downtown Portland)482<br>Wexley Street, Portland, ME 04109,</p>
  </section>

  <section class="schedule">
    <div class="schedule-item schedule-date">
      <svg width="26" height="24" viewBox="0 0 26 24" aria-hidden="true">
        <rect x="1.5" y="3.5" width="23" height="19" fill="none" stroke="var(--brand-orange)" stroke-width="2"/>
        <rect x="1.5" y="3.5" width="23" height="5" fill="var(--brand-orange)"/>
        <g fill="var(--brand-orange)"><rect x="5" y="11" width="3" height="3"/><rect x="11" y="11" width="3" height="3"/><rect x="17" y="11" width="3" height="3"/><rect x="5" y="16" width="3" height="3"/><rect x="11" y="16" width="3" height="3"/><rect x="17" y="16" width="3" height="3"/></g>
      </svg>
      <span>August 8th, 9th, 10th and 11th, 2019</span>
    </div>
    <div class="schedule-item schedule-time">
      <svg width="28" height="28" viewBox="0 0 28 28" aria-hidden="true">
        <circle cx="14" cy="14" r="13" fill="var(--brand-orange)"/>
        <path d="M14 7v8h6" fill="none" stroke="#fff" stroke-width="2.5"/>
      </svg>
      <span>7:00PM</span>
    </div>
  </section>

  <footer class="contact-bar">
    <div class="contact-item contact-phone">
      <svg width="22" height="34" viewBox="0 0 22 34" aria-hidden="true">
        <path d="M8 2 C2 6 2 26 9 32 L13 30 L10 22 L7 23 C5 18 5 14 7 10 L10 11 L12 3 Z" fill="#fff"/>
      </svg>
      <span>207 555 3184</span>
    </div>
    <div class="contact-item contact-email">
      <svg width="34" height="22" viewBox="0 0 34 22" aria-hidden="true">
        <rect x="1" y="1" width="32" height="20" fill="none" stroke="#fff" stroke-width="2"/>
        <path d="M1 1 L17 13 L33 1 M1 21 L13 10 M33 21 L21 10" fill="none" stroke="#fff" stroke-width="2"/>
      </svg>
      <span>contact@meadowcrest.org</span>
    </div>
    <div class="contact-item contact-web">
      <svg width="22" height="22" viewBox="0 0 22 22" aria-hidden="true">
        <g fill="none" stroke="#fff" stroke-width="1.8"><circle cx="11" cy="11" r="9.5"/><ellipse cx="11" cy="11" rx="4" ry="9.5"/><path d="M1.5 11h19M3 6h16M3 16h16"/></g>
      </svg>
      <span>www.vostel.org</span>
    </div>
  </footer>
</main>
</body>
</html>
```